integrative health clinic-Medical massage, acupuncture, chiropractic

we like our logo, but are open to new ideas. We need a new card design. We have added chiropractic and acupuncture that we have put under the name of the business. We are an integrative medical clinic

Target Market(s)

General public, athletes

Contact Information for Business Card

Phone 5055583927
Fax 5055583926
Hours Monday-Friday 9-6
Saturday 10-6
The 20% can be smaller on the back

Colors
3176b5
0355a3

Requirements
Must have
• Logo but am open to ideas
Nice to have
• We are an integrated medical clinic but also want to be personable. We want the card fun and inviting

```html
<!DOCTYPE html>
<html lang="en">
<head>
<meta charset="utf-8">
<title>Open Range Wellness – Business Cards</title>
<link href="https://fonts.googleapis.com/css2?family=Lato:wght@400;700&family=Crimson+Text:ital@1&display=swap" rel="stylesheet">
<style>
  :root {
    --brand-blue: #0355a3;
    --brand-blue-light: #3176b5;
    --ink-blue: #1f5fae;
    --white: #ffffff;
    --backdrop: #8f8d8e;
    --photo-dark: #1b1b1b;
    --photo-tan: #c9a576;
    --photo-grey: #cfcfcf;
    --photo-grey-dark: #6f6f6f;
  }
  * { margin: 0; padding: 0; box-sizing: border-box; }
  html, body { width: 1200px; height: 880px; overflow: hidden; }
  body {
    background: radial-gradient(ellipse at center, #d2d1d1 0%, var(--backdrop) 100%);
    font-family: "Lato", sans-serif;
    position: relative;
  }
  .card {
    position: absolute;
    width: 560px;
    height: 320px;
    border-radius: 18px;
    overflow: hidden;
    box-shadow: 0 8px 22px rgba(0,0,0,0.25);
  }
  .card--offer {
    left: 60px; top: 80px;
    background: linear-gradient(160deg, var(--brand-blue) 0%, var(--brand-blue-light) 100%);
    color: var(--white);
  }
  .card--contact {
    left: 580px; top: 480px;
    background: var(--white);
    color: var(--ink-blue);
  }
  .card__photo { position: absolute; inset: 0; width: 100%; height: 100%; }
  .brand {
    position: absolute;
    display: flex;
    align-items: center;
    gap: 10px;
  }
  .brand__dot {
    width: 38px; height: 38px; border-radius: 50%;
    flex: none;
  }
  .card--offer .brand__dot { background: var(--white); }
  .card--contact .brand__dot { background: var(--brand-blue); }
  .brand__name {
    font-family: "Lato", sans-serif;
    font-weight: 700;
    font-size: 27px;
    line-height: 1;
    letter-spacing: -0.5px;
  }
  .brand__tagline {
    font-family: "Crimson Text", serif;
    font-style: italic;
    font-size: 14px;
    margin-top: 3px;
  }
  .card--contact .brand__tagline { color: #333; }
  .offer {
    position: absolute; left: 40px; top: 120px;
    font-weight: 700; font-size: 17px; letter-spacing: 3px;
  }
  .details {
    position: absolute; left: 40px; top: 156px;
    font-size: 15px; line-height: 1.3;
  }
  .details__gap { margin-top: 10px; }
  .details__lead { font-size: 18px; }
  .services {
    position: absolute; left: 40px; top: 100px;
    font-size: 17px; line-height: 1.2;
  }
  .address {
    position: absolute; left: 40px; top: 170px;
    font-size: 17px; line-height: 1.2;
  }
  .contact-list {
    position: absolute; left: 40px; top: 222px;
    list-style: none;
    font-size: 16px; line-height: 1.3;
  }
  .contact-list li { display: flex; align-items: center; gap: 8px; }
  .contact-list svg { width: 15px; height: 15px; flex: none; }
</style>
</head>
<body>

<section class="card card--offer">
  <svg class="card__photo" viewBox="0 0 560 320" role="img" aria-label="Photo of acupuncture needles being placed in skin">
    <defs>
      <linearGradient id="needlePhoto" x1="0" y1="0" x2="0" y2="1">
        <stop offset="0" stop-color="var(--photo-dark)"/>
        <stop offset="0.55" stop-color="#2a2420"/>
        <stop offset="0.62" stop-color="var(--photo-tan)"/>
        <stop offset="1" stop-color="#d9b98c"/>
      </linearGradient>
    </defs>
    <path d="M330 0 H560 V320 H440 C340 270 300 170 320 70 C326 40 330 20 330 0 Z" fill="url(#needlePhoto)"/>
  </svg>
  <div class="brand" style="left:36px; top:40px;">
    <span class="brand__dot"></span>
    <div>
      <div class="brand__name">Open Range Wellness</div>
      <div class="brand__tagline">Sports Therapy and Wellness Center</div>
    </div>
  </div>
  <p class="offer">20% OFF FIRST VISIT</p>
  <div class="details">
    <p>We accept some insurance<br>workers Comp and Personal Injury</p>
    <p class="details__gap details__lead">Book Online</p>
    <p>www.openrangewellnessnm.com</p>
    <p class="details__gap">Hours<br>Monday-Friday 9-6<br>Saturday 10-6</p>
  </div>
</section>

<section class="card card--contact">
  <svg class="card__photo" viewBox="0 0 560 320" role="img" aria-label="Photo of a man holding his neck and lower back with the spine highlighted">
    <defs>
      <radialGradient id="backPhoto" cx="0.7" cy="0.45" r="0.6">
        <stop offset="0" stop-color="var(--photo-grey-dark)"/>
        <stop offset="0.6" stop-color="#a9a9a9"/>
        <stop offset="1" stop-color="var(--photo-grey)"/>
      </radialGradient>
    </defs>
    <path d="M290 0 H560 V320 H470 C360 300 290 230 280 130 C275 80 280 40 290 0 Z" fill="url(#backPhoto)"/>
  </svg>
  <div class="brand" style="left:36px; top:32px;">
    <span class="brand__dot"></span>
    <div>
      <div class="brand__name">Open Range Wellness</div>
      <div class="brand__tagline">Sports Therapy and Wellness Center</div>
    </div>
  </div>
  <p class="services">Specializing in Medical<br>Sports massage<br>and ManualTherapies</p>
  <p class="address">1450 Cerrillos Ln. Suite 4<br>santa Fe, NM 87505</p>
  <ul class="contact-list">
    <li>
      <svg viewBox="0 0 16 16" aria-hidden="true"><circle cx="8" cy="8" r="7.5" fill="var(--ink-blue)"/><path d="M5 4.5 L7 6.5 L6 7.5 Q7 9.5 8.5 10 L9.5 9 L11.5 11 L10.5 12 Q6 11.5 4 6 Z" fill="#fff"/></svg>
      5055583927
    </li>
    <li>
      <svg viewBox="0 0 16 16" aria-hidden="true"><circle cx="8" cy="8" r="7.5" fill="var(--ink-blue)"/><rect x="4.5" y="6.5" width="7" height="4.5" fill="#fff"/><rect x="5.5" y="4" width="5" height="2.5" fill="#fff"/></svg>
      5055583926
    </li>
    <li>
      <svg viewBox="0 0 16 16" aria-hidden="true"><circle cx="8" cy="8" r="7.5" fill="var(--ink-blue)"/><rect x="4" y="5" width="8" height="6" fill="#fff"/><path d="M4 5 L8 8.5 L12 5" stroke="var(--ink-blue)" fill="none" stroke-width="1"/></svg>
      Info@openrangewellnessnm.com
    </li>
    <li>
      <svg viewBox="0 0 16 16" aria-hidden="true"><circle cx="8" cy="8" r="7.5" fill="var(--ink-blue)"/><circle cx="8" cy="8" r="4.5" fill="none" stroke="#fff"/><ellipse cx="8" cy="8" rx="2" ry="4.5" fill="none" stroke="#fff"/><line x1="3.5" y1="8" x2="12.5" y2="8" stroke="#fff"/></svg>
      www.openrangewellnessnm.com
    </li>
  </ul>
</section>

</body>
</html>
```